Poster Design Project

Im looking to have a poster for a theatrical magic show made. my style is classic throw back on the darker more adult side, mysterious, master magician, Slick,slick,slick no ones better,top dollar ticket price,sexy, vintage marquee lights spelling out VELMONTE,I wear a fitted black suit, old berlin cabaret feel.artistic first class upscale I hope tis description helps if you need more info please email me.
Updates

poster should be 24" by  36" 

Target Market(s)

all ages all cultures

Industry/Entity Type

Adult

Requirements
Must have
• my name VELMONTE in vintage marquee lights, a picture of my face upfront. a darker vintage style.broadwaysish cabaret
Nice to have
• can you crop the pic so you only see my face and hand. poster size 24" by 36"

I prefer: VELMONTE up top in the Marquee lettering (with yellowish-white theatrical broadway bulbs that look like they are really lit. Kind of a Harold Brisbey effect.)

Then, the Duncan Fairlow quote in the middle:

Duncan Fairlow ~ "ABSOLUTELY BRILLIANT!!!" (His name should be in the same font used on his WBX TV Show.)

Then, at the bottom:
MASTER MAGICIAN
(Maybe, the K in King can be replaced by the King of hearts playing card)
Should not have
• rabbits,canes, wands no no no thanks

```html
<!DOCTYPE html>
<html lang="en">
<head>
<meta charset="utf-8">
<title>VELMONTE – Master Magician</title>
<link rel="stylesheet" href="https://fonts.googleapis.com/css2?family=Archivo+Black&family=Roboto+Condensed:wght@400;700&family=Montserrat:wght@500&display=swap">
<style>
  :root {
    --ink: #02040a;
    --bulb: #fff36a;
    --paper: #ffffff;
    --ghost-fill: #1a2a57;
    --ghost-edge: #3d548c;
    --gold: #f2d431;
  }
  html, body {
    margin: 0;
    padding: 0;
    width: 800px;
    height: 1200px;
    overflow: hidden;
    background: var(--ink);
  }
  .poster {
    display: block;
    width: 800px;
    height: 1200px;
  }
  .marquee-title {
    font-family: "Archivo Black", sans-serif;
    fill: none;
    stroke: var(--bulb);
    stroke-width: 10;
    stroke-linecap: round;
    stroke-dasharray: 0 16;
  }
  .quote-line {
    font-family: "Roboto Condensed", sans-serif;
    font-weight: 700;
    fill: var(--paper);
  }
  .quote-credit {
    font-family: "Roboto Condensed", sans-serif;
    font-weight: 400;
    fill: var(--paper);
  }
  .ghost-name {
    font-family: "Archivo Black", sans-serif;
    fill: var(--ghost-fill);
    stroke: var(--ghost-edge);
    stroke-width: 2;
    opacity: 0.8;
  }
  .billing {
    font-family: "Montserrat", sans-serif;
    font-weight: 500;
    fill: var(--gold);
  }
</style>
</head>
<body>
<svg class="poster" viewBox="0 0 800 1200" xmlns="http://www.w3.org/2000/svg">
  <defs>
    <linearGradient id="stage-night" x1="0" y1="0" x2="0" y2="1">
      <stop offset="0" stop-color="#02040a"/>
      <stop offset="0.45" stop-color="#071333"/>
      <stop offset="1" stop-color="#02040a"/>
    </linearGradient>
    <radialGradient id="suit-tone" cx="0.3" cy="0.55" r="0.65">
      <stop offset="0" stop-color="#1d3470"/>
      <stop offset="0.6" stop-color="#0c1a40"/>
      <stop offset="1" stop-color="#02040a" stop-opacity="0"/>
    </radialGradient>
    <radialGradient id="face-tone" cx="0.5" cy="0.45" r="0.5">
      <stop offset="0" stop-color="#a9bde8"/>
      <stop offset="0.45" stop-color="#5d7cc0"/>
      <stop offset="0.8" stop-color="#25407f"/>
      <stop offset="1" stop-color="#0c1a40" stop-opacity="0"/>
    </radialGradient>
    <radialGradient id="hand-tone" cx="0.5" cy="0.5" r="0.5">
      <stop offset="0" stop-color="#9db2e2"/>
      <stop offset="0.5" stop-color="#4f6db2"/>
      <stop offset="0.85" stop-color="#1c3270"/>
      <stop offset="1" stop-color="#02040a" stop-opacity="0"/>
    </radialGradient>
    <filter id="bulb-glow" x="-10%" y="-30%" width="120%" height="160%">
      <feGaussianBlur in="SourceGraphic" stdDeviation="4" result="blur"/>
      <feMerge>
        <feMergeNode in="blur"/>
        <feMergeNode in="SourceGraphic"/>
      </feMerge>
    </filter>
  </defs>

  <rect class="backdrop" width="800" height="1200" fill="url(#stage-night)"/>

  <g class="portrait" role="img" aria-label="Blue-toned portrait of the magician in a dark fitted suit: his face at left and his open hand reaching toward the viewer at right">
    <ellipse class="portrait-suit" cx="260" cy="780" rx="420" ry="420" fill="url(#suit-tone)"/>
    <ellipse class="portrait-face" cx="175" cy="590" rx="175" ry="240" fill="url(#face-tone)"/>
    <ellipse class="portrait-hand" cx="640" cy="680" rx="150" ry="100" fill="url(#hand-tone)"/>
  </g>

  <text class="ghost-name" x="0" y="0" font-size="96" text-anchor="middle"
        transform="translate(490 880) rotate(-58) skewX(-12)">VELMONTE</text>

  <text class="marquee-title" x="400" y="210" font-size="130" text-anchor="middle"
        textLength="612" lengthAdjust="spacingAndGlyphs" filter="url(#bulb-glow)">VELMONTE</text>

  <g class="review">
    <text class="quote-line" x="715" y="426" font-size="64" text-anchor="end"
          textLength="288" lengthAdjust="spacingAndGlyphs">ABSOLUTELY</text>
    <text class="quote-line" x="715" y="488" font-size="64" text-anchor="end"
          textLength="252" lengthAdjust="spacingAndGlyphs">BRILLIANT!!!</text>
    <text class="quote-credit" x="715" y="512" font-size="18" text-anchor="end">~ DUNCAN FAIRLOW</text>
  </g>

  <text class="billing" x="403" y="1100" font-size="46" text-anchor="middle"
        textLength="592" lengthAdjust="spacing">MASTER MAGICIAN</text>
</svg>
</body>
</html>
```